Core values in our company OPK (Residency and Relocation)

Do good:
1. Being Direct and communicative for the benefit of all parties
2. Working for the Benefit of the company, client and team members
3. Wanting to improve to create a better impact
4. Having healthy rivalry
Be ahead of curve:
1. Having the confidence to break through barriers which arise
2. Desire to grow and learn towards establishment and agreed goal
3. Getting off the sidelines and get into the game
4. Keeping the end game in mind having due regard to processes and milestones
5. Self starter and works on own initiative
6. Diligent and impactful in your field of responsibility
Truth and Honesty
2. Have the confidence and ability to speak what you really want to communicate
3. Being truthful to yourself, clients and colleagues to find the innovations that lie within
4. Seeking the truth by opening things up for discussion
5. Being Optimistic
Background Information on our Company:OPK is a professional law firm in London Docklands. We caters for both private and corporate clients ranging from highly regarded and established law firms to boutique and niche immigration practices. We also specialises in expert legal advice and prides itself on providing services that go beyond the expectations of its clients.
What we need: We need a Poster about Truth and Honesty, this is to show one of our values as a company. It will need to be vibrant and straight to the point. Colours can be orange grey white and yellow. Attached is our company logo.
Reason: To remind colleagues that this is one of our main values and it is instilled in our company.
Things we would like:
1. To create a point of focus
2. Use shapes to create visual interest
3. Use creative illustrations
4. Take the viewer’s focus on a journey with clever perspective
Industry/Entity Type
Legal
Requirements
Must have
- a globe (Picture)
- Do good:
- 1. Being Direct and communicative for the benefit of all parties
- 2. Working for the Benefit of the company, client and team members
- 3. Wanting to improve to create a better impact
- 4. Having healthy rivalry
- Be ahead of curve:
- 1. Having the confidence to break through barriers which arise
- 2. Desire to grow and learn towards establishment and agreed goal
- 3. Getting off the sidelines and get into the game
- 4. Keeping the end game in mind having due regard to processes and milestones
- 5. Self starter and works on own initiative
- 6. Diligent and impactful in your field of responsibility
- Truth and Honesty
- 2. Have the confidence and ability to speak what you really want to communicate
- 3. Being truthful to yourself, clients and colleagues to find the innovations that lie within
- 4. Seeking the truth by opening things up for discussion
- 5. Being Optimistic

```html
<!DOCTYPE html>
<html lang="en">
<head>
<meta charset="utf-8">
<title>OPK Truth and Honesty Poster</title>
<link rel="stylesheet" href="https://fonts.googleapis.com/css2?family=EB+Garamond:wght@400;500;600&display=swap">
<style>
  :root {
    --grey-dark: #4a4a4c;
    --orange: #f67c1a;
    --yellow: #f2e21b;
    --white: #ffffff;
    --ink: #0c0c0c;
    --photo-deep: #1f1c1a;
    --photo-mid: #4b4642;
    --photo-light: #6d6762;
    --globe-light: #7fa6c4;
    --globe-deep: #2c4d68;
  }
  html, body {
    margin: 0;
    padding: 0;
    overflow: hidden;
    background: var(--white);
  }
  .poster {
    position: relative;
    width: 848px;
    height: 1200px;
    overflow: hidden;
    background: var(--white);
    font-family: "EB Garamond", Georgia, serif;
  }
  .poster__shapes {
    position: absolute;
    inset: 0;
    width: 848px;
    height: 1200px;
  }
  .headline {
    position: absolute;
    margin: 0;
    line-height: 1;
    font-weight: 500;
  }
  .headline--truth {
    left: 60px;
    top: 140px;
    font-size: 200px;
    letter-spacing: 8px;
    color: var(--white);
    text-shadow: 6px 6px 0 var(--ink), 8px 9px 6px rgba(0,0,0,0.35);
  }
  .headline--honesty {
    right: 48px;
    top: 340px;
    font-size: 104px;
    letter-spacing: 2px;
    color: var(--ink);
  }
  .values {
    position: absolute;
    left: 58px;
    top: 716px;
    width: 430px;
    margin: 0;
    padding: 0;
    list-style: none;
    color: var(--white);
    font-size: 24px;
    font-weight: 600;
    line-height: 33px;
    text-shadow: 1px 1px 3px rgba(0,0,0,0.6);
  }
  .values__item {
    display: flex;
    gap: 10px;
    margin-bottom: 16px;
  }
  .values__num {
    color: var(--yellow);
    flex: none;
  }
  .brand {
    position: absolute;
    left: 514px;
    top: 960px;
    width: 290px;
    text-align: center;
    color: var(--white);
    font-weight: 500;
    margin: 0;
  }
  .brand__name {
    display: block;
    font-size: 112px;
    line-height: 130px;
  }
  .brand__tagline {
    display: block;
    font-size: 24px;
    line-height: 30px;
    margin-top: 14px;
  }
</style>
</head>
<body>
<main class="poster">
  <svg class="poster__shapes" viewBox="0 0 848 1200" xmlns="http://www.w3.org/2000/svg">
    <defs>
      <linearGradient id="photo-tone" x1="0" y1="0" x2="1" y2="1">
        <stop offset="0" stop-color="var(--photo-mid)"/>
        <stop offset="0.45" stop-color="var(--photo-light)"/>
        <stop offset="1" stop-color="var(--photo-deep)"/>
      </linearGradient>
      <radialGradient id="globe-tone" cx="0.38" cy="0.35" r="0.7">
        <stop offset="0" stop-color="var(--globe-light)"/>
        <stop offset="1" stop-color="var(--globe-deep)"/>
      </radialGradient>
    </defs>
    <polygon class="band band--grey" points="0,0 360,0 0,192" fill="var(--grey-dark)"/>
    <polygon class="band band--orange" points="360,0 848,0 848,252 0,668 0,192" fill="var(--orange)"/>
    <polygon class="photo" role="img" aria-label="Close-up of a hand writing with a pen on documents at a desk" points="0,690 848,432 848,1200 0,1200" fill="url(#photo-tone)"/>
    <circle class="globe" role="img" aria-label="Globe of the world" cx="664" cy="770" r="125" fill="url(#globe-tone)"/>
  </svg>

  <h1 class="headline headline--truth">TRUTH</h1>
  <p class="headline headline--honesty">&amp; HONESTY</p>

  <ol class="values">
    <li class="values__item"><span class="values__num">2.</span><span>Have the confidence and ability to speak what you really want to communicate</span></li>
    <li class="values__item"><span class="values__num">3.</span><span>Being truthful to yourself, clients and colleagues to find the innovations that lie within</span></li>
    <li class="values__item"><span class="values__num">4.</span><span>Seeking the truth by opening things up for discussion</span></li>
    <li class="values__item"><span class="values__num">5.</span><span>Being Optimistic</span></li>
  </ol>

  <p class="brand">
    <span class="brand__name">OPK</span>
    <span class="brand__tagline">Residency and Relocation</span>
  </p>
</main>
</body>
</html>
```